Australian Software Consultancy needs new Business Card Design

Design Business Card based on existing design artefacts (attached). We are open to all designs. As its a 2 sided design and we thought it might be quite striking to have one side with a black background and te other side with a white background.

Target Market(s)

Financial Services mainly.

Industry/Entity Type

Business

Contact Information for Business Card

Requirements
Must have
• Funky design using our existing assets

```html
<!DOCTYPE html>
<html lang="en">
<head>
<meta charset="utf-8">
<title>North Field – Business Card</title>
<link href="https://fonts.googleapis.com/css2?family=Roboto:wght@400;700;900&display=swap" rel="stylesheet">
<style>
  :root {
    --stage: #5d666b;
    --stage-light: #79838a;
    --ink: #050505;
    --paper: #ffffff;
    --accent: #e8222a;
    --light-text: #f2f2f2;
  }
  html, body {
    margin: 0;
    width: 1200px;
    height: 900px;
    overflow: hidden;
  }
  body {
    background: radial-gradient(ellipse at 60% 35%, var(--stage-light), var(--stage) 75%);
    font-family: "Roboto", Arial, sans-serif;
    position: relative;
  }
  .card {
    position: absolute;
    left: 290px;
    width: 620px;
    height: 354px;
    border-radius: 18px;
    overflow: hidden;
    box-shadow: 0 14px 30px rgba(0,0,0,.45);
  }
  .card--front { top: 56px; background: var(--ink); }
  .card--back  { top: 470px; background: var(--ink); }

  .front-shapes { position: absolute; inset: 0; }

  .brand {
    position: absolute;
    left: 42px;
    top: 34px;
    margin: 0;
    font-weight: 900;
    font-size: 40px;
    letter-spacing: 1px;
    color: var(--ink);
  }
  .contact {
    position: absolute;
    left: 60px;
    top: 150px;
    list-style: none;
    margin: 0;
    padding: 0;
    font-size: 15px;
    color: var(--ink);
  }
  .contact li {
    display: flex;
    align-items: center;
    gap: 8px;
    height: 22px;
  }
  .contact-icon { width: 16px; height: 16px; flex: none; }

  .person {
    position: absolute;
    left: 345px;
    top: 44px;
    color: var(--light-text);
  }
  .person-name {
    margin: 0;
    font-weight: 700;
    font-size: 24px;
    letter-spacing: .5px;
  }
  .person-role {
    margin: 2px 0 0;
    font-size: 12px;
    letter-spacing: .5px;
  }
  .address {
    position: absolute;
    left: 340px;
    top: 200px;
    margin: 0;
    font-style: normal;
    font-size: 16px;
    line-height: 1.35;
    color: var(--light-text);
  }

  .back-mark {
    position: absolute;
    inset: 0;
    display: flex;
    align-items: center;
    justify-content: center;
    gap: 16px;
  }
  .back-dot {
    width: 34px;
    height: 34px;
    border-radius: 50%;
    background: var(--accent);
  }
  .back-name {
    margin: 0;
    font-weight: 900;
    font-size: 44px;
    letter-spacing: 1px;
    color: var(--accent);
  }
</style>
</head>
<body>

<section class="card card--front" aria-label="Card front">
  <svg class="front-shapes" width="620" height="354" viewBox="0 0 620 354" aria-hidden="true">
    <polygon points="0,0 348,0 222,354 0,354" fill="var(--paper)"/>
    <polygon points="314,34 560,34 520,110 286,110" fill="var(--accent)"/>
  </svg>

  <h1 class="brand">NORTH FIELD</h1>

  <ul class="contact">
    <li>
      <svg class="contact-icon" viewBox="0 0 16 16" aria-hidden="true">
        <rect width="16" height="16" fill="var(--accent)"/>
        <path d="M5 3.5l2 2-1 1.2c.6 1.3 1.6 2.3 2.9 2.9l1.2-1 2 2-1.3 1.6C7.8 11.9 4.1 8.2 3.4 4.8z" fill="#fff"/>
      </svg>
      (617)555-0148
    </li>
    <li>
      <svg class="contact-icon" viewBox="0 0 16 16" aria-hidden="true">
        <rect width="16" height="16" fill="var(--accent)"/>
        <rect x="3" y="4.5" width="10" height="7" fill="none" stroke="#fff" stroke-width="1.2"/>
        <path d="M3 4.5l5 4 5-4" fill="none" stroke="#fff" stroke-width="1.2"/>
      </svg>
      ella@northfield.co
    </li>
  </ul>

  <div class="person">
    <h2 class="person-name">ELLA MARSH</h2>
    <p class="person-role">OWNER</p>
  </div>

  <address class="address">48 Harbor Lane<br>Boston MA 02110</address>
</section>

<section class="card card--back" aria-label="Card back">
  <div class="back-mark">
    <span class="back-dot" aria-hidden="true"></span>
    <p class="back-name">NORTH FIELD</p>
  </div>
</section>

</body>
</html>
```